Logo & Visitenkarte für Einzelunternehmen
Zielgruppe
Einzelunternehmen: Dienstleistung für Sanitär, Heizung, Solar
Aufgabenstellung
Das Design soll einen hohen Wiedererkennungswert in der Sanitär-Heizung-Branche bzw. vor allem bei Privatpersonen aufweisen.
'als der Ansprechpartner vor Ort / in der Umgebung gelten'

```html
<!DOCTYPE html>
<html lang="de">
<head>
<meta charset="utf-8">
<title>Lukas Brenning – Logo &amp; Visitenkarte</title>
<link rel="stylesheet" href="https://fonts.googleapis.com/css2?family=Montserrat:wght@600;700;800&family=Roboto:wght@400&display=swap">
<style>
  :root {
    --sheet: #e6e6e6;
    --ink: #111111;
    --brand-blue: #0d5ea8;
    --card-dark: #1c1c1c;
    --heat-red: #cc0e12;
    --heat-orange: #f39200;
    --tag-grey: #555555;
    --white: #ffffff;
  }
  * { box-sizing: border-box; margin: 0; padding: 0; }
  html, body { width: 918px; height: 1200px; overflow: hidden; background: var(--sheet); }
  .sheet { position: relative; width: 918px; height: 1200px; font-family: "Roboto", Arial, sans-serif; }

  /* logo presentation tile */
  .logo-tile {
    position: absolute; left: 365px; top: 36px; width: 479px; height: 257px;
    background: var(--white); border-radius: 0 0 62px 62px;
    box-shadow: 0 6px 14px rgba(0,0,0,.18);
  }
  .wordmark {
    position: absolute; font-family: "Montserrat", sans-serif; font-weight: 800;
    color: var(--brand-blue); line-height: 1.02; letter-spacing: .5px;
  }
  .logo-tile .wordmark { left: 70px; top: 42px; font-size: 46px; }
  .tagline {
    position: absolute; font-family: "Montserrat", sans-serif; font-weight: 700;
    line-height: 1.25; padding: 3px 5px;
  }
  .logo-tile .tagline {
    left: 70px; top: 164px; width: 309px; height: 43px;
    background: var(--tag-grey); color: var(--white); font-size: 13.4px; padding: 4px 5px;
  }

  /* labels */
  .variant-label { position: absolute; font-size: 35px; color: var(--ink); left: 530px; }
  .side-label { position: absolute; left: 52px; font-size: 36px; color: var(--ink); letter-spacing: 1px; }
  .side-arrow { position: absolute; left: 194px; width: 106px; height: 24px; }

  /* business cards */
  .card {
    position: absolute; left: 372px; width: 428px; height: 276px; overflow: hidden;
    box-shadow: 0 8px 14px rgba(0,0,0,.22);
  }
  .card-front { top: 491px; }
  .card-back { top: 897px; }
  .card-art { position: absolute; inset: 0; width: 428px; height: 276px; }
  .card .wordmark { font-size: 25px; }
  .card .tagline { background: var(--white); color: var(--card-dark); font-size: 8.6px; padding: 2px 4px; }

  .card-front .wordmark { left: 30px; top: 34px; }
  .card-front .tagline { left: 30px; top: 102px; width: 190px; height: 26px; }
  .radiator-art {
    position: absolute; left: 267px; top: 63px; width: 89px; height: 115px;
    border-radius: 6px; background: linear-gradient(180deg, var(--heat-red), var(--heat-orange));
  }
  .person-name {
    position: absolute; left: 29px; top: 150px; font-family: "Montserrat", sans-serif;
    font-weight: 700; font-size: 19px; color: var(--white);
  }
  .person-role { position: absolute; left: 29px; top: 172px; font-size: 11.5px; color: var(--white); }
  .contact { position: absolute; display: flex; align-items: flex-start; gap: 8px; font-size: 10.5px; color: var(--white); line-height: 1.2; }
  .contact svg { width: 12px; height: 12px; flex: none; fill: var(--white); }
  .contact-address { left: 29px; top: 197px; }
  .contact-email { left: 29px; top: 238px; }
  .contact-phone { left: 264px; top: 199px; }
  .contact-fax { left: 264px; top: 217px; }
  .contact-mobile { left: 264px; top: 236px; }

  .card-back .wordmark { left: 110px; top: 88px; }
  .card-back .tagline { left: 110px; top: 156px; width: 197px; height: 28px; font-size: 9px; }
</style>
</head>
<body>
<div class="sheet">

  <section class="logo-tile">
    <div class="wordmark">LUKAS<br>BRENNING</div>
    <div class="tagline">SANITÄR. HEIZUNG. SOLARANLAGEN.<br>WARTUNGEN. REPARATUR</div>
  </section>

  <div class="variant-label" style="top:392px">A-1</div>

  <div class="side-label" style="top:600px">FRONT</div>
  <svg class="side-arrow" style="top:609px" viewBox="0 0 106 24"><rect x="0" y="10.5" width="84" height="3" fill="#111"/><path d="M78 1 L106 12 L78 23 L84 12 Z" fill="#111"/></svg>

  <article class="card card-front">
    <svg class="card-art" viewBox="0 0 744 480" preserveAspectRatio="none" aria-hidden="true">
      <defs>
        <linearGradient id="heatFront" x1="0" y1="0" x2="0" y2="1">
          <stop offset="0" stop-color="#cc0e12"/><stop offset=".25" stop-color="#cc0e12"/>
          <stop offset=".72" stop-color="#f39200"/><stop offset="1" stop-color="#f39200"/>
        </linearGradient>
      </defs>
      <rect width="744" height="480" fill="url(#heatFront)"/>
      <path d="M0 0 H521 C560 95 625 170 650 250 C675 330 630 390 540 405 C420 420 230 405 0 365 Z" fill="#1c1c1c"/>
    </svg>
    <div class="wordmark">LUKAS<br>BRENNING</div>
    <div class="tagline">SANITÄR. HEIZUNG. SOLARANLAGEN.<br>WARTUNGEN. REPARATUR</div>
    <div class="radiator-art" role="img" aria-label="Illustration eines Heizkörpers mit aufsteigenden Wärmewellen"></div>
    <div class="person-name">Carla Vendrami</div>
    <div class="person-role">Geschäftsführerin, Dipl. Kauffrau</div>
    <div class="contact contact-address">
      <svg viewBox="0 0 12 12"><path d="M6 0a4.3 4.3 0 0 0-4.3 4.3C1.7 7.5 6 12 6 12s4.3-4.5 4.3-7.7A4.3 4.3 0 0 0 6 0zm0 6.2a1.9 1.9 0 1 1 0-3.8 1.9 1.9 0 0 1 0 3.8z"/></svg>
      <span>Lindenhof-Str. 14<br>55299 Feldbach</span>
    </div>
    <div class="contact contact-email">
      <svg viewBox="0 0 12 12"><path d="M0 2h12v8H0z M0 2l6 5 6-5" fill="none" stroke="#fff" stroke-width="1.2"/></svg>
      <span>lukasbrenning@hausnetz-mail.de</span>
    </div>
    <div class="contact contact-phone">
      <svg viewBox="0 0 12 12"><path d="M2.4 0.5l2 2.4-1.1 1.4c.7 1.6 2 2.9 3.5 3.6l1.4-1.1 2.4 2-1.3 2.2C5 10.6 1.2 6.8.3 2z"/></svg>
      <span>+0 61 34 / 27 18</span>
    </div>
    <div class="contact contact-fax">
      <svg viewBox="0 0 12 12"><path d="M3 0h6v3H3z M0 4h12v5H0z M3 7h6v5H3z"/></svg>
      <span>0 61 34 / 27 19</span>
    </div>
    <div class="contact contact-mobile">
      <svg viewBox="0 0 12 12"><path d="M3 0h6a1 1 0 0 1 1 1v10a1 1 0 0 1-1 1H3a1 1 0 0 1-1-1V1a1 1 0 0 1 1-1zm0.5 1.5v8h5v-8z"/></svg>
      <span>01 72 / 4 38 60 21</span>
    </div>
  </article>

  <div class="variant-label" style="top:832px">B-1</div>

  <div class="side-label" style="top:1012px">BACK</div>
  <svg class="side-arrow" style="top:1021px" viewBox="0 0 106 24"><rect x="0" y="10.5" width="84" height="3" fill="#111"/><path d="M78 1 L106 12 L78 23 L84 12 Z" fill="#111"/></svg>

  <article class="card card-back">
    <svg class="card-art" viewBox="0 0 744 480" preserveAspectRatio="none" aria-hidden="true">
      <defs>
        <linearGradient id="heatBack" x1="0" y1="0" x2="0" y2="1">
          <stop offset="0" stop-color="#cc0e12"/><stop offset=".25" stop-color="#cc0e12"/>
          <stop offset=".72" stop-color="#f39200"/><stop offset="1" stop-color="#f39200"/>
        </linearGradient>
      </defs>
      <rect width="744" height="480" fill="url(#heatBack)"/>
      <path d="M0 0 H521 C560 95 625 170 650 250 C675 330 630 390 540 405 C420 420 230 405 0 365 Z" fill="#1c1c1c"/>
    </svg>
    <div class="wordmark">LUKAS<br>BRENNING</div>
    <div class="tagline">SANITÄR. HEIZUNG. SOLARANLAGEN.<br>WARTUNGEN. REPARATUR</div>
  </article>

</div>
</body>
</html>
```